Web Design Project

I'm looking for a web design that incorporates the content included below into a web site that is clearly for a platform as a service product that helps people build complex web information systems that also do mobile apps and integrations.
Updates

Project Deadline Extended
Reason: I would like to encourage more submissions so I'm extending the deadline. Designs submitted earlier may win due to immediate need for some collateral. We will be posting several other contests in the near future if this one goes well.

Here are some sample web sites we like quite a lot:

http://www.plovra.com
http://www.zenthark.com/
http://www.zenthark.com/skyvault/ipaas-cloud-based-integration-demand
http://www.quorvelnet.com/hybrid-it

It is really important that the first 5 graphic panels in the word document get translated into a rotating banner for the home page.

Our software integrates databases, services, social-media, security, and mobile devices, but it starts with building great web applications for the desktop and real integrated systems for businesses. We also integrate accounting, CRM, and lots of other things together - that's important.

We focus on creating one system. Please try to capture that concept. Don't deliver just mobile - we're system first, and mobile second. The goal is to help our customers merge all their systems into one.

Target Market(s)

CIOs, CTOs, Technical Decision Makers, Business People

Industry/Entity Type

Build

Requirements
Must have
• Home Page that introduces the product and what it can do for people. Product Page that shows options for the product: Platform as a Service and Licensing. Services page that shows options for Services - Virtual Development Teams and Professional Services. A Blog Page. About Us Page with location info, contact info, etc.
Nice to have
• Scrolling home page banners. Lead generation - Contact us form.

```html
<!DOCTYPE html>
<html lang="en">
<head>
<meta charset="utf-8">
<title>Kindlepoint Technologies</title>
<link href="https://fonts.googleapis.com/css2?family=Roboto+Condensed:wght@400;700&family=Arimo:wght@400;700&display=swap" rel="stylesheet">
<style>
:root{
  --page:#ececec;
  --white:#ffffff;
  --red:#d4302b;
  --orange:#e07a33;
  --orange-dark:#b9561d;
  --ink:#333333;
  --nav:#6b6b6b;
  --navy:#1d4f80;
  --hero-a:#eef6f7;
  --hero-b:#d8e9ec;
  --dark:#3a3a3a;
  --btn:#2f2f2f;
  --icon:#a9a9a9;
}
*{margin:0;padding:0;box-sizing:border-box}
html,body{width:1126px;height:1200px;overflow:hidden}
body{background:var(--page);font-family:"Arimo",Arial,sans-serif;color:var(--ink);position:relative}

/* header */
.site-header{position:absolute;left:0;top:0;width:1126px;height:89px;background:linear-gradient(#fafafa,#f1f1f1)}
.header-rule{position:absolute;left:0;top:89px;width:1126px;height:3px;background:var(--red)}
.brand{position:absolute;display:flex;align-items:center;gap:8px;font-family:"Roboto Condensed",Arial,sans-serif;font-weight:700;color:#555}
.brand-dot{border-radius:50%;background:var(--orange)}
.brand--header{left:113px;top:24px;font-size:30px}
.brand--header .brand-dot{width:34px;height:34px}
.main-nav a{position:absolute;top:60px;font-size:12.5px;letter-spacing:.5px;color:var(--nav);text-decoration:none}
.nav-pointer{position:absolute;left:550px;top:83px;width:0;height:0;border-left:7px solid transparent;border-right:7px solid transparent;border-bottom:7px solid var(--red)}

/* hero */
.hero{position:absolute;left:96px;top:92px;width:934px;height:377px;background:linear-gradient(160deg,var(--hero-a),var(--hero-b));box-shadow:0 8px 10px -6px rgba(0,0,0,.25)}
.brand--hero{left:804px;top:12px;font-size:17px;gap:5px}
.brand--hero .brand-dot{width:20px;height:20px}
.hero-title{position:absolute;left:28px;top:29px;width:560px;font-family:"Roboto Condensed",Arial,sans-serif;font-size:32px;line-height:39px;color:#5a5a5a;font-weight:400}
.hero-title em{font-style:normal;color:var(--orange)}
.feature-list{position:absolute;left:28px;top:168px;list-style:none}
.feature-list li{display:flex;align-items:center;gap:9px;font-size:15px;font-weight:700;color:#4a4a4a;height:35.5px}
.price{position:absolute;left:304px;top:196px;width:270px;height:110px}
.price-cloud{position:absolute;left:60px;top:20px;width:170px;height:90px;border-radius:50%;background:radial-gradient(#ffffff 55%,rgba(255,255,255,0) 72%)}
.price-start{position:absolute;left:0;top:60px;font-size:17px;font-weight:700;color:#555}
.price-amount{position:absolute;left:56px;top:8px;font-weight:700;color:#111;white-space:nowrap}
.price-amount .cur{font-size:40px;vertical-align:top;position:relative;top:28px}
.price-amount .big{font-size:72px;letter-spacing:-2px}
.price-amount .cents{font-size:40px}
.price-mo{position:absolute;left:196px;top:60px;font-size:17px;color:#444}
.price-tag{position:absolute;left:196px;top:0;width:46px;height:36px;background:#fbf1c8;transform:rotate(-14deg);font-size:12px;font-weight:700;line-height:13px;text-align:center;padding-top:5px;color:#333;box-shadow:0 1px 2px rgba(0,0,0,.25)}
.devices-art{position:absolute;left:561px;top:49px;width:318px;height:206px;border-radius:18px;background:radial-gradient(ellipse at 50% 45%,#d4682c 0%,#e89a66 45%,rgba(220,236,240,0) 75%)}
.hero-rule{position:absolute;left:64px;top:323px;width:860px;height:1px;background:#b8c9cc}
.cta{position:absolute;left:366px;top:297px;width:211px;height:50px;background:var(--orange);border-bottom:3px solid var(--orange-dark);color:#fff;font-weight:700;font-size:22px;display:flex;align-items:center;justify-content:center;box-shadow:0 2px 4px rgba(0,0,0,.2)}

/* features */
.features{position:absolute;left:96px;top:469px;width:934px;height:315px;background:var(--white);border-bottom:1px solid #d6dadb}
.feature{position:absolute;top:38px;width:284px;text-align:center;transform:translateX(-50%)}
.feature svg{display:block;margin:0 auto;height:64px}
.feature h2{font-family:"Roboto Condensed",Arial,sans-serif;font-weight:400;font-size:31px;color:var(--red);margin-top:6px;line-height:34px}
.feature h3{font-weight:400;font-size:19px;color:#444;margin-top:2px;line-height:24px}
.feature p{font-size:12.5px;line-height:17px;color:#444;margin-top:6px}
.btn{display:inline-block;background:var(--btn);color:#fff;font-size:13.5px;padding:5px 14px;border-radius:3px;box-shadow:0 2px 3px rgba(0,0,0,.3);white-space:nowrap}
.feature .btn{margin-top:12px}

/* one system */
.system{position:absolute;left:96px;top:784px;width:934px;height:332px;background:linear-gradient(#e6f5f8,#ffffff 75%)}
.system h2{position:absolute;left:32px;top:40px;font-weight:400;font-size:32px;color:var(--navy)}
.system p{position:absolute;left:33px;top:96px;width:445px;font-size:14px;line-height:20.6px;color:#555}
.system .btn{position:absolute;left:32px;top:236px}
.system-art{position:absolute;left:530px;top:18px;width:350px;height:270px;border-radius:50%;background:radial-gradient(ellipse at 50% 50%,#b9d3ea 0%,#dbe8f2 45%,rgba(230,245,248,0) 72%)}

/* footer */
.site-footer{position:absolute;left:0;top:1090px;width:1126px;height:110px;background:var(--dark)}
.footer-panel{position:absolute;left:96px;top:1088px;width:934px;height:28px;background:var(--white)}
.footer-nav{position:absolute;left:98px;top:1138px;font-size:12px;color:#fff;font-weight:700;word-spacing:2px}
.footer-nav span{margin:0 8px;font-weight:400}
.copyright{position:absolute;left:98px;top:1161px;font-size:12px;color:#fff}
.brand--footer{left:826px;top:1134px;font-size:27px;color:#cfcfcf}
.brand--footer .brand-dot{width:32px;height:32px;background:#8a8a8a}
</style>
</head>
<body>

<header class="site-header">
  <div class="brand brand--header"><span class="brand-dot"></span>KINDLEPOINT</div>
  <nav class="main-nav">
    <a style="left:538px">HOME</a>
    <a style="left:634px">PLATFORM</a>
    <a style="left:758px">SERVICES</a>
    <a style="left:873px">BLOG</a>
    <a style="left:965px">ABOUT US</a>
  </nav>
  <span class="nav-pointer"></span>
</header>
<div class="header-rule"></div>

<section class="hero">
  <div class="brand brand--hero"><span class="brand-dot"></span>KINDLEPOINT</div>
  <h1 class="hero-title"><em>Create custom enterprise</em> software where you need it connecting customers and partners to you.</h1>
  <ul class="feature-list">
    <li><svg width="20" height="20" viewBox="0 0 20 20"><circle cx="10" cy="10" r="8" fill="none" stroke="#3b77b6" stroke-width="2"/><path d="M5.5 10l3.5 3.5L17 4" fill="none" stroke="#24446b" stroke-width="2.5"/></svg>Unlimited Storage</li>
    <li><svg width="20" height="20" viewBox="0 0 20 20"><circle cx="10" cy="10" r="8" fill="none" stroke="#3b77b6" stroke-width="2"/><path d="M5.5 10l3.5 3.5L17 4" fill="none" stroke="#24446b" stroke-width="2.5"/></svg>Unlimited Monthly Bandwidth</li>
    <li><svg width="20" height="20" viewBox="0 0 20 20"><circle cx="10" cy="10" r="8" fill="none" stroke="#3b77b6" stroke-width="2"/><path d="M5.5 10l3.5 3.5L17 4" fill="none" stroke="#24446b" stroke-width="2.5"/></svg>CGI, PHP, RoR and MySQL</li>
  </ul>
  <div class="price">
    <div class="price-cloud"></div>
    <div class="price-start">Start</div>
    <div class="price-amount"><span class="cur">$</span><span class="big">3</span><span class="cents">.98</span></div>
    <div class="price-mo">/mo</div>
    <div class="price-tag">30%<br>OFF</div>
  </div>
  <div class="devices-art" role="img" aria-label="Illustration of a tablet and two phones in orange cases showing list screens, over soft clouds"></div>
  <div class="hero-rule"></div>
  <div class="cta">Get Started Now</div>
</section>

<section class="features">
  <div class="feature" style="left:168px">
    <svg viewBox="0 0 64 64" width="64"><g fill="var(--icon)"><path d="M12 8l8 2 30 30 6 2-2 6-6-2L18 16z"/><path d="M50 6a10 10 0 0 0-10 13L10 49l5 5 30-30A10 10 0 0 0 58 14l-6 5-5-2-1-5 6-6z"/></g></svg>
    <h2>Customizable</h2>
    <h3>Modify anything instantly</h3>
    <p>Built-in theme customizer allows you to change theme's settings in real-time without even having to save options and reload the page. You can change everything from colors to header.</p>
    <span class="btn">Try it out now</span>
  </div>
  <div class="feature" style="left:483px">
    <svg viewBox="0 0 64 64" width="64"><g fill="var(--icon)"><path d="M32 2a17 17 0 0 0-11 30c3 3 4 7 4 11h14c0-4 1-8 4-11A17 17 0 0 0 32 2z"/><rect x="24" y="46" width="16" height="3" rx="1"/><rect x="24" y="51" width="16" height="3" rx="1"/><rect x="26" y="56" width="12" height="4" rx="2"/></g></svg>
    <h2>Versatile</h2>
    <h3>More than meets the eye</h3>
    <p>Built-in theme customizer allows you to change theme's settings in real-time without even having to save options and reload the page. You can change everything.</p>
    <span class="btn">See other pages</span>
  </div>
  <div class="feature" style="left:772px">
    <svg viewBox="0 0 64 64" width="64"><g fill="var(--icon)"><path d="M32 2c-8 8-11 18-11 30l2 16h18l2-16c0-12-3-22-11-30z"/><path d="M21 34l-9 10v12l10-8zM43 34l9 10v12l-10-8z"/><rect x="29" y="50" width="6" height="12" rx="2"/></g><circle cx="32" cy="26" r="5" fill="#fff"/></svg>
    <h2>Responsive</h2>
    <h3>Any device, anywhere</h3>
    <p>Built-in theme customizer allows you to change theme's settings in real-time without even having to save options and reload the page. You can change everything .</p>
    <span class="btn">Find out more</span>
  </div>
</section>

<section class="system">
  <h2>One Business. One System.</h2>
  <p>Document how your business works and translate that into a consistent user experience across all your channels. Let Kindlepoint close the gap on features and control how your business works and translate that into a consistent user experience across all your channels. Let Kindlepoint close the gap on features and control from your “One Business” model.from your “One Business” model.</p>
  <span class="btn">See other pages</span>
  <div class="system-art" role="img" aria-label="Illustration of a central system hub linked to documents, devices, security, cloud, API and social channel icons"></div>
</section>

<div class="site-footer"></div>
<div class="footer-panel"></div>
<div class="footer-nav">Home<span>~</span>Platform<span>~</span>Services<span>~</span>Blog<span>~</span>About Us</div>
<div class="copyright">Copyright © 2013 kindlepoint. All right reserved</div>
<div class="brand brand--footer"><span class="brand-dot"></span>KINDLEPOINT</div>

</body>
</html>
```